Lotvantage.com Webpage Design

Design Brief for lotvantage.com (Copy of Brief also in attached Word file)

Name of Website- lotvantage.com (existing logo and look & feel of website to be changed)

Logo - Finalised. The logo files are attached with the brief as “logo.jpeg”. The “Blue- Grey” version of the logo is for use on lighter backgrounds and the “Orange-White” version of the logo is for use on darker backgrounds. (A full Black version of the logo is also attached). Both versions may be used in different parts of the website. All attached files are in .png format.
Status - The website in functional and is undergoing user trials. However, we want to improve the look & feel of the website so at it seems
a. cotemporary,
b. Easy to Navigate
c. professional and
d. Vibrant.

Please visit ‘lotvantage.com’ to check out the website and its functionalities – please use it only as a reference for the features & functions to be provided, however the designer should use a ‘Free Hand’ in designing the composition of various parts of the webpage without getting too influenced by the existing design

Objective of the Website ‘lotvantage.com –
a. It is a portal focussed on listing of ‘Retail’ specific real-estate properties by developers, owners and realty brokers. The properties shall listed under the following four categories-
i. Retail Malls
ii. Shopping Complexes
iii. High-street shops
iv. Retail Warehouses
*refer lotvantage.com for better clarity

b. The abovementioned properties shall be listed either for ‘Sale’ or ‘rent\lease’ or both

c. Users shall visit the site in case they wish to acquire a retail \ shop space either on ‘sale’ or ‘rent’. These Users would be able to specify the ‘Search Criteria’ through the tool-bars provided on the website – the ‘Search Criteria’ shall comprise of ‘Type of space category’, ‘City’, ‘Locality’, transaction type ie ‘Rent \ Sale’ and ‘Area Range’

d. The main revenue model for the website shall be listing fee ( or advertising charges ) payable by those listing their properties on the website.

Three Main Pages of Website (lotvantage.com) that need to be designed -
a. Main Home Page (visit the web link - http://lotvantage.com/ ) - The main home page has the “Search Toolbar” for specifying of Search Criteria by the User. It shall also have the following features & functions-
i. Main Advertising Banner
ii. Featured Projects
iii. New Launches
iv. Toolbar with buttons – ‘Advertise with Us’, ‘Listings Alert’, ‘Lot Mavens’, ‘Advertiser Login’

b. Property Listings Page (visit the web link - http://lotvantage.com/gurgaon-in-india ) - The List of property options that match the Criteria specified by the ‘User’ get displayed on this page.

c. Property Detail Page - When the ‘User’ clicks on the “More….” Button on the ‘Property Listings Page’ (given in point b. above) the web page with the details of the property opens. (For Example – visit the web link - http://lotvantage.com/brevo-Shopping-Complex-brevo-quadrel-gurgaon-636 )

Note:- Please refer to attached ‘Shopping’ related images the designer may use them on the website to provide a look & feel of retail if required – either separately or rotate in a single window

Target Market(s)

Retailers & Investors looking for retail space, Real Estate Brokers, Developers

Industry/Entity Type

Advertising

Number of Pages Required

3 page

Requirements
Must have
• Refer to existing site lotvantage.com -- all the existing functionalities are a must have.
Nice to have
• The Designer may use the retail related images on the website if required for making it more vibrant. Refer attached images Shopping(1-6).jpg

```html
<!DOCTYPE html>
<html lang="en">
<head>
<meta charset="utf-8">
<title>Lotvantage.com – Retail Spaces Across India</title>
<link href="https://fonts.googleapis.com/css2?family=Open+Sans:wght@400;600;700&display=swap" rel="stylesheet">
<style>
:root{
  --blue:#1e7fc6;
  --navy:#1b2431;
  --navy-2:#252f3d;
  --orange:#f39a1e;
  --page:#eceff2;
  --card:#ffffff;
  --line:#d5dbe1;
  --text:#2b333d;
  --muted:#6b7580;
  --white:#ffffff;
}
*{box-sizing:border-box;margin:0;padding:0}
html,body{width:1200px;height:2216px;overflow:hidden}
body{font-family:"Open Sans",Arial,sans-serif;color:var(--text);background:var(--page);font-size:12px;position:relative}

/* hero */
.hero{position:absolute;left:0;top:0;width:1200px;height:520px;overflow:hidden}
.hero-photo{position:absolute;inset:0;background:linear-gradient(180deg,#8d99a6 0%,#aab3bc 35%,#6f7a86 70%,#4b5561 100%)}
.hero-shade{position:absolute;inset:0;background:linear-gradient(180deg,rgba(20,28,38,.55) 0,rgba(20,28,38,.05) 100px,rgba(20,28,38,.05) 380px,rgba(20,28,38,.45) 520px)}

.brand{position:absolute;left:206px;top:20px;display:flex;align-items:center;gap:10px}
.brand-mark{width:30px;height:30px;border-radius:50%;background:var(--orange)}
.brand-name{font-size:28px;font-weight:700;color:var(--white);letter-spacing:-.5px}

.top-links{position:absolute;right:206px;top:16px;display:flex;gap:12px;align-items:center;font-size:11px;color:var(--white)}
.top-links .region{border:1px solid rgba(255,255,255,.6);padding:2px 8px}
.main-nav{position:absolute;right:206px;top:48px;display:flex;font-size:12px}
.main-nav a{color:var(--white);text-decoration:none;padding:6px 10px;border-left:1px solid rgba(255,255,255,.35)}
.main-nav a:first-child{border-left:none}
.main-nav a.active{background:var(--blue)}

.search{position:absolute;left:232px;top:224px;width:736px}
.search-tabs{display:flex;gap:4px;margin-left:40px}
.search-tabs span{width:72px;text-align:center;padding:6px 0;background:rgba(255,255,255,.85);font-weight:600;font-size:13px;color:var(--navy)}
.search-tabs span.active{background:var(--blue);color:var(--white)}
.search-panel{background:rgba(27,36,49,.82);padding:10px 40px 12px}
.search-fields{display:flex;gap:10px;align-items:flex-end}
.field{display:flex;flex-direction:column;gap:3px}
.field label{font-size:10px;color:#c9d1d9}
.field .box{height:26px;background:var(--white);border:1px solid var(--line);font-size:11px;color:var(--muted);padding:5px 8px;display:flex;justify-content:space-between}
.field .box::after{content:"▾";color:var(--muted)}
.field .box.plain::after{content:""}
.btn-search{height:26px;padding:0 16px;background:var(--blue);color:var(--white);font-weight:700;font-size:11px;display:flex;align-items:center}

.quick-bar{display:flex;justify-content:space-between;background:rgba(255,255,255,.9);padding:6px 60px;font-size:11px}
.quick-bar div{text-align:center}
.quick-bar b{display:block;color:var(--navy);font-weight:700}
.quick-bar small{color:var(--muted);font-size:9px}

/* categories */
.categories{position:absolute;left:0;top:520px;width:1200px;height:80px;background:var(--navy);display:flex;justify-content:center;gap:80px;align-items:center}
.category{text-align:center;padding:0 10px}
.category b{display:block;color:var(--orange);font-size:14px;font-weight:600}
.category small{color:#b8c1cb;font-size:10px}

/* listings */
.section-title{position:absolute;left:206px;font-size:18px;font-weight:700;color:var(--navy)}
.section-title span{font-size:12px;font-weight:400;color:var(--muted)}
.grid{position:absolute;left:206px;width:788px;display:grid;grid-template-columns:repeat(3,252px);gap:14px 16px}
.card{background:var(--card);border:1px solid var(--line);height:210px;padding:6px}
.card-photo{height:128px;background:linear-gradient(180deg,#7fa7cf 0%,#c9d7e3 55%,#8c939b 100%)}
.card-body{display:flex;justify-content:space-between;padding:5px 2px 0}
.card-city{font-size:15px;font-weight:700;color:var(--blue);line-height:1.2}
.card-name{font-size:11px;font-weight:600;color:var(--text)}
.card-meta{font-size:10px;color:var(--muted);line-height:1.35}
.card-btn{align-self:flex-start;margin-top:2px;background:var(--blue);color:var(--white);font-size:9px;padding:3px 7px;white-space:nowrap}
.view-all{position:absolute;left:206px;background:var(--navy);color:var(--white);font-size:11px;padding:5px 14px}

/* lower */
.lower{position:absolute;left:206px;top:1720px;width:788px;display:grid;grid-template-columns:1fr 1fr;gap:0 40px}
.lower h3{font-size:16px;font-weight:700;color:var(--navy);margin-bottom:6px}
.lower p{font-size:10px;color:var(--muted);line-height:1.5;margin-bottom:8px}
.input-row{display:flex;gap:6px}
.input{width:230px;height:24px;background:var(--white);border:1px solid var(--line);font-size:10px;color:var(--muted);padding:5px 8px}
.btn{background:var(--blue);color:var(--white);font-size:10px;padding:5px 12px;display:inline-block}
.btn-dark{background:var(--navy)}
.block{margin-bottom:22px}

/* footer */
.footer{position:absolute;left:0;top:2064px;width:1200px;height:152px;background:var(--navy)}
.footer-inner{position:absolute;left:206px;top:16px;width:788px;display:grid;grid-template-columns:190px 180px 200px 1fr;color:#c2cad3;font-size:10px;line-height:1.5}
.footer h4{color:var(--white);font-size:12px;margin-bottom:4px}
.footer .brand-foot{display:flex;align-items:center;gap:6px;color:var(--white);font-weight:700;font-size:18px}
.footer .brand-foot i{width:18px;height:18px;border-radius:50%;background:var(--orange)}
.social{display:flex;gap:6px;margin-bottom:6px}
.social i{width:20px;height:20px;border-radius:50%;background:var(--navy-2);border:1px solid #56616e}
.copyright{position:absolute;left:0;bottom:0;width:1200px;height:22px;background:#141b25;color:#8995a2;font-size:9px;text-align:center;line-height:22px}
</style>
</head>
<body>

<header class="hero">
  <div class="hero-photo" role="img" aria-label="City skyline of high-rise commercial towers"></div>
  <div class="hero-shade"></div>
  <div class="brand"><span class="brand-mark"></span><span class="brand-name">lotvantage</span></div>
  <div class="top-links"><span>Advertiser Login</span><span class="region">All India ▾</span></div>
  <nav class="main-nav">
    <a class="active">Home</a><a>About Us</a><a>Featured Projects</a><a>New Launches</a><a>Contact Us</a>
  </nav>

  <div class="search">
    <div class="search-tabs"><span class="active">Sale</span><span>Rent</span><span>Both</span></div>
    <div class="search-panel">
      <div class="search-fields">
        <div class="field"><label>Retail Space</label><div class="box" style="width:110px">Retail Malls</div></div>
        <div class="field"><label>Select City</label><div class="box" style="width:100px">Select</div></div>
        <div class="field"><label>Select Locality/Area</label><div class="box" style="width:150px">Select</div></div>
        <div class="field"><label>Enter Keywords</label><div class="box plain" style="width:160px">Project/Name/Builder</div></div>
        <div class="btn-search">SEARCH</div>
      </div>
    </div>
    <div class="quick-bar">
      <div><b>Advertise with us</b><small>List your retail property</small></div>
      <div><b>Lot Mavens</b><small>Talk to our space experts</small></div>
      <div><b>Listing Alert</b><small>Get new listings by email</small></div>
    </div>
  </div>
</header>

<section class="categories">
  <div class="category"><b>Retail Malls</b><small>Curated mall spaces</small></div>
  <div class="category"><b>Shopping Complex</b><small>Ready &amp; upcoming units</small></div>
  <div class="category"><b>High Street Shops</b><small>Prime road frontage</small></div>
  <div class="category"><b>Retail Warehouses</b><small>Bulk storage spaces</small></div>
</section>

<h2 class="section-title" style="top:644px">Featured Retail Projects <span>(Across India)</span></h2>
<div class="grid" style="top:680px">
  <div class="card"><div class="card-photo" role="img" aria-label="Retail project building exterior"></div><div class="card-body"><div><div class="card-city">Surat</div><div class="card-name">Velmora Arcade</div><div class="card-meta">Ring Road<br>Shopping Complex</div></div><span class="card-btn">View full listing</span></div></div>
  <div class="card"><div class="card-photo" role="img" aria-label="Retail project building exterior"></div><div class="card-body"><div><div class="card-city">Faridabad</div><div class="card-name">Orin Plaza</div><div class="card-meta">Sector 42<br>Shopping Complex</div></div><span class="card-btn">View full listing</span></div></div>
  <div class="card"><div class="card-photo" role="img" aria-label="Retail project building exterior"></div><div class="card-body"><div><div class="card-city">Gurgaon</div><div class="card-name">Kestrel Square</div><div class="card-meta">Sector 19<br>Shopping Complex</div></div><span class="card-btn">View full listing</span></div></div>
  <div class="card"><div class="card-photo" role="img" aria-label="Retail project building exterior"></div><div class="card-body"><div><div class="card-city">Surat</div><div class="card-name">Velmora Arcade</div><div class="card-meta">Ring Road<br>Shopping Complex</div></div><span class="card-btn">View full listing</span></div></div>
  <div class="card"><div class="card-photo" role="img" aria-label="Retail project building exterior"></div><div class="card-body"><div><div class="card-city">Pune</div><div class="card-name">Orin Plaza</div><div class="card-meta">Sector 42<br>Shopping Complex</div></div><span class="card-btn">View full listing</span></div></div>
  <div class="card"><div class="card-photo" role="img" aria-label="Retail project building exterior"></div><div class="card-body"><div><div class="card-city">Hyderabad</div><div class="card-name">Kestrel Square</div><div class="card-meta">Sector 19<br>Shopping Complex</div></div><span class="card-btn">View full listing</span></div></div>
</div>
<span class="view-all" style="top:1132px">View all</span>

<h2 class="section-title" style="top:1180px">Featured New Launches <span>(Across India)</span></h2>
<div class="grid" style="top:1216px">
  <div class="card"><div class="card-photo" role="img" aria-label="New launch building exterior"></div><div class="card-body"><div><div class="card-city">Surat</div><div class="card-name">Velmora Arcade</div><div class="card-meta">Ring Road<br>Shopping Complex</div></div><span class="card-btn">View full listing</span></div></div>
  <div class="card"><div class="card-photo" role="img" aria-label="New launch building exterior"></div><div class="card-body"><div><div class="card-city">Faridabad</div><div class="card-name">Orin Plaza</div><div class="card-meta">Sector 42<br>Shopping Complex</div></div><span class="card-btn">View full listing</span></div></div>
  <div class="card"><div class="card-photo" role="img" aria-label="New launch building exterior"></div><div class="card-body"><div><div class="card-city">Gurgaon</div><div class="card-name">Kestrel Square</div><div class="card-meta">Sector 19<br>Shopping Complex</div></div><span class="card-btn">View full listing</span></div></div>
  <div class="card"><div class="card-photo" role="img" aria-label="New launch building exterior"></div><div class="card-body"><div><div class="card-city">Vijayawada</div><div class="card-name">Velmora Arcade</div><div class="card-meta">Ring Road<br>Shopping Complex</div></div><span class="card-btn">View full listing</span></div></div>
  <div class="card"><div class="card-photo" role="img" aria-label="New launch building exterior"></div><div class="card-body"><div><div class="card-city">Faridabad</div><div class="card-name">Orin Plaza</div><div class="card-meta">Sector 42<br>Shopping Complex</div></div><span class="card-btn">View full listing</span></div></div>
  <div class="card"><div class="card-photo" role="img" aria-label="New launch building exterior"></div><div class="card-body"><div><div class="card-city">Hyderabad</div><div class="card-name">Kestrel Square</div><div class="card-meta">Sector 19<br>Shopping Complex</div></div><span class="card-btn">View full listing</span></div></div>
</div>
<span class="view-all" style="top:1668px">View all</span>

<section class="lower">
  <div>
    <div class="block">
      <h3>Listing Alert</h3>
      <p>Sign up for free listing alert updates on new listings at lotvantage.com</p>
      <div class="input-row"><div class="input">Enter your email address</div><span class="btn">Submit</span></div>
    </div>
    <div class="block">
      <h3>Lot Mavens</h3>
      <p>Post your retail space requirement with us and our experts shall get back with suitable options and help you close your transaction.</p>
      <div class="input-row"><div class="input">Enter your email address</div><span class="btn">Submit</span></div>
    </div>
  </div>
  <div>
    <div class="block">
      <h3>Editor's Choice</h3>
      <p>A select listing of retail properties handpicked by our editorial team based on location, footfall potential, developer track record and long-term value for both retailers and investors across India's growing cities.</p>
      <span class="btn btn-dark">More</span>
    </div>
    <div class="block">
      <h3>What is lotvantage.com?</h3>
      <p>Lotvantage.com is a specialised portal for retail real estate, listing malls, shopping complexes, high street shops and retail warehouses for sale or rent by developers, owners and brokers.</p>
      <span class="btn btn-dark">More</span>
    </div>
  </div>
</section>

<footer class="footer">
  <div class="footer-inner">
    <div><div class="brand-foot"><i></i>lotvantage</div></div>
    <div><h4>Address</h4>Kestrel Tower, 4th Floor<br>Sector 14, Gurgaon<br>Haryana - 122001</div>
    <div><h4>Company</h4>About Us<br>Privacy Policy<br>Terms of Use<br>Contact Us<br>Site Map</div>
    <div><h4>Follow Us</h4><div class="social"><i></i><i></i><i></i><i></i></div>T: 000-123-4567</div>
  </div>
  <div class="copyright">Copyright © lotvantage.com. All rights reserved.</div>
</footer>

</body>
</html>
```